PowerPoint template for my training workshop business

I would like to have a PowerPoint template created using my logo and palette materials created by Brindlework. I train and facilitate workshops using PowerPoint in both corporate and public settings.

I have attached the original design elements to this request.

```html
<!DOCTYPE html>
<html lang="en">
<head>
<meta charset="utf-8">
<title>Marisa Dell Coaching – Workshop Slide Template</title>
<link href="https://fonts.googleapis.com/css2?family=Cinzel:wght@600;700&family=Uncial+Antiqua&family=Poppins:wght@400;500;600&display=swap" rel="stylesheet">
<style>
:root{
  --orange:#f7941d;
  --orange-deep:#ef7d12;
  --yellow:#fdc93c;
  --yellow-soft:#fdd866;
  --teal:#0d3c45;
  --plum:#5c1b4b;
  --plum-bright:#6a1b52;
  --slate:#868ca0;
  --lavender:#a9b1d6;
  --ink:#222;
  --muted:#666;
  --paper:#fff;
  --sheet:#fff;
}
*{box-sizing:border-box;margin:0;padding:0}
html,body{width:771px;height:1200px;overflow:hidden;background:var(--sheet)}
body{position:relative;font-family:"Poppins",Arial,sans-serif;color:var(--ink)}

.brand{position:absolute;left:0;right:0;top:28px;text-align:center;font-family:"Poppins",Arial,sans-serif;font-weight:600;font-size:24px;color:var(--teal);line-height:1}

.slide{position:absolute;width:236px;height:133px;overflow:hidden;background:var(--paper);box-shadow:0 2px 5px rgba(0,0,0,.22)}
.c1{left:11px}.c2{left:268px}.c3{left:525px}
.r1{top:82px}.r2{top:240px}.r3{top:398px}.r4{top:555px}.r5{top:713px}.r6{top:871px}.r7{top:1028px}
.abs{position:absolute}
.ph{position:absolute}

.title{font-family:"Cinzel",serif;font-weight:700;color:var(--ink);position:absolute;white-space:nowrap}
.display{font-family:"Uncial Antiqua",serif;color:var(--orange);position:absolute;line-height:1.02}
.tiny{font-size:3px;line-height:1.35;color:var(--muted)}
.small{font-size:3.6px;line-height:1.35}
.lead{font-size:4.4px;font-weight:600;color:var(--orange)}

.foot{position:absolute;left:0;right:0;bottom:3px;height:8px}
.foot .mini{position:absolute;left:20px;top:1.5px;font-family:"Poppins",Arial,sans-serif;font-weight:600;font-size:2.8px;color:var(--orange);white-space:nowrap}
.foot .url{position:absolute;left:100px;top:2px;font-size:2.2px;color:var(--muted)}
.foot .pg{position:absolute;right:14px;top:0;width:7px;height:7px;border-radius:50%;border:.8px solid var(--orange);font-size:3px;color:var(--ink);text-align:center;line-height:5.6px}
.foot.dark .url{color:var(--orange)}
.foot.dark .pg{color:#fff}

.mlogo{position:absolute;font-family:"Poppins",Arial,sans-serif;font-weight:600;color:var(--orange);font-size:3.4px;line-height:1;white-space:nowrap}

.num{position:absolute;width:10px;height:10px;border-radius:50%;background:var(--orange);color:#fff;font-size:4px;font-weight:600;text-align:center;line-height:10px}
.ring{position:absolute;width:16px;height:16px;border-radius:50%;border:1px solid var(--orange);background:#fff}
.ring::after{content:"";position:absolute;inset:3px;border-radius:50%;border:.8px solid var(--orange)}
.dot{position:absolute;width:5px;height:5px;border-radius:50%;border:1.4px solid var(--orange);background:#fff}

.cell{position:absolute;color:#fff;padding:3px 4px}
.cell b{display:block;font-size:3.4px;font-weight:600;margin-bottom:2px}
.cell p{font-size:2.6px;line-height:1.35}
</style>
</head>
<body>

<div class="brand">Marisa Dell Coaching</div>

<!-- 1 cover -->
<section class="slide c1 r1">
  <div class="ph" style="left:0;top:0;width:92px;height:133px;background:linear-gradient(140deg,#3f5a2a,#8aa064 55%,#2d3d1e);border-right:6px solid var(--orange);border-radius:0 70px 70px 0" role="img" aria-label="Photo of a woman with closed eyes among green foliage"></div>
  <div class="mlogo" style="left:112px;top:52px;font-size:8px;color:var(--teal)">Marisa Dell Coaching</div>
  <div class="display" style="left:118px;top:72px;font-size:8.5px;text-align:center;width:100px">WORKSHOP<br>EMBRACING BODY,<br>MIND &amp; SPIRIT</div>
  <div class="foot"><span class="url">www.marisadellcoaching.com</span></div>
</section>

<!-- 2 guiding principles -->
<section class="slide c2 r1">
  <div class="ph" style="left:0;top:0;width:88px;height:133px;background:linear-gradient(160deg,#e8e8e6,#8b8b87 60%,#3a3a38)" role="img" aria-label="Photo of a bright office with laptops by a window"></div>
  <div class="abs" style="left:44px;top:40px;width:60px;height:60px;border-radius:50%;background:#fff;box-shadow:0 1px 4px rgba(0,0,0,.25)"></div>
  <div class="title" style="left:66px;top:9px;font-size:9px">GUIDING PRINCIPLES</div>
  <div class="ring" style="left:117px;top:29px"></div>
  <div class="ring" style="left:126px;top:51px"></div>
  <div class="ring" style="left:126px;top:73px"></div>
  <div class="ring" style="left:117px;top:95px"></div>
  <p class="abs tiny" style="left:144px;top:31px;width:72px">Lorem No ceteros verterem his, sea eius iisque eu. Et vis stet dolorem perpetua, usu ea diam affert labores</p>
  <p class="abs tiny" style="left:154px;top:53px;width:66px">Lorem No ceteros verterem his, sea eius iisque eu. Et vis stet dolorem perpetua, usu ea diam affert labores</p>
  <p class="abs tiny" style="left:153px;top:75px;width:67px">Lorem No ceteros verterem his, sea eius iisque eu. Et vis stet dolorem perpetua, usu ea diam affert labores.</p>
  <p class="abs tiny" style="left:144px;top:97px;width:72px">Lorem No ceteros verterem his, sea eius iisque eu. Et vis stet dolorem perpetua, usu ea diam affert labores.</p>
  <div class="foot"><span class="url">www.marisadellcoaching.com</span><span class="pg">2</span></div>
</section>

<!-- 3 contents -->
<section class="slide c3 r1">
  <div class="ph" style="left:0;top:0;width:84px;height:133px;background:linear-gradient(160deg,#b9a7b3,#8c7f84 55%,#6c6a62)" role="img" aria-label="Soft-focus photo of a woman among blossoms"></div>
  <div class="title" style="left:18px;top:62px;font-size:8px;color:#fff">CONTENTS</div>
  <div class="mlogo" style="left:184px;top:10px;font-size:3px">Marisa Dell</div>
  <div class="num" style="left:111px;top:19px">1</div>
  <div class="num" style="left:111px;top:40px">2</div>
  <div class="num" style="left:111px;top:60px">3</div>
  <div class="num" style="left:111px;top:81px">4</div>
  <div class="num" style="left:111px;top:102px">5</div>
  <div class="abs" style="left:129px;top:20px;font-size:3.6px"><b style="font-family:Cinzel,serif;color:var(--plum)">INTRODUCTION</b><br><span style="color:var(--orange)">Before starting</span></div>
  <div class="abs" style="left:129px;top:41px;font-size:3.6px"><b style="font-family:Cinzel,serif;color:var(--plum)">ABOUT US</b><br><span style="color:var(--orange)">What we did, what we do</span></div>
  <div class="abs" style="left:129px;top:61px;font-size:3.6px"><b style="font-family:Cinzel,serif;color:var(--plum)">OUR PORTFOLIO</b><br><span style="color:var(--orange)">Our amazing products</span></div>
  <div class="abs" style="left:129px;top:82px;font-size:3.6px"><b style="font-family:Cinzel,serif;color:var(--plum)">NEW PROPOSAL</b><br><span style="color:var(--orange)">Our awesome ideas</span></div>
  <div class="abs" style="left:129px;top:103px;font-size:3.6px;width:50px"><b style="font-family:Cinzel,serif;color:var(--plum)">ANALYSIS</b><br><span style="color:var(--orange)">Marketing data and our estimation</span></div>
  <div class="foot"><span class="url">www.marisadellcoaching.com</span><span class="pg">3</span></div>
</section>

<!-- 4 about our workshop -->
<section class="slide c1 r2">
  <div class="abs" style="left:0;top:0;width:236px;height:133px;background:var(--lavender)"></div>
  <div class="abs" style="left:76px;top:-20px;width:240px;height:175px;border-radius:50% 0 0 50%;background:linear-gradient(90deg,#fff,#f2f2f2)"></div>
  <div class="title" style="left:7px;top:57px;font-size:8px;color:#fff;line-height:1.2">ABOUT OUR<br>WORKSHOP</div>
  <div class="mlogo" style="left:184px;top:10px;font-size:3px">Marisa Dell</div>
  <div class="abs" style="left:113px;top:25px;width:80px">
    <p style="font-size:5px;color:var(--teal)">• Lorem No ceteros verterem</p>
    <p class="tiny" style="padding-left:6px;margin-bottom:6px">No ceteros verterem his, sea eius iisque eu. Et vis stet dolorem perpetua, usu ea diam affert</p>
    <p style="font-size:5px;color:var(--teal)">• Lorem No ceteros verterem</p>
    <p class="tiny" style="padding-left:6px;margin-bottom:6px">No ceteros verterem his, sea eius iisque eu. Et vis stet dolorem perpetua, usu ea diam affert</p>
    <p style="font-size:5px;color:var(--teal)">• Lorem No ceteros verterem</p>
    <p class="tiny" style="padding-left:6px;margin-bottom:6px">No ceteros verterem his, sea eius iisque eu. Et vis stet dolorem perpetua, usu ea diam affert</p>
    <p style="font-size:5px;color:var(--teal)">• Lorem No ceteros verterem</p>
    <p class="tiny" style="padding-left:6px">No ceteros verterem his, sea eius iisque eu. Et vis stet dolorem perpetua, usu ea diam affert</p>
  </div>
  <div class="foot"><span class="url">www.marisadellcoaching.com</span><span class="pg">5</span></div>
</section>

<!-- 5 about workshop yellow -->
<section class="slide c2 r2">
  <div class="ph" style="left:0;top:0;width:236px;height:133px;background:linear-gradient(180deg,#d9e2e6,#6d8a8a 45%,#3d5a55 70%,#5a4a3a)" role="img" aria-label="Photo of a person sitting at the end of a wooden pier on a mountain lake"></div>
  <div class="abs" style="left:-60px;top:-30px;width:180px;height:195px;border-radius:50%;background:var(--yellow-soft)"></div>
  <div class="abs" style="left:0;top:0;width:60px;height:133px;background:var(--yellow-soft)"></div>
  <div class="display" style="left:19px;top:39px;font-size:9px;color:var(--teal)">ABOUT OUR<br>WORKSHOP</div>
  <p class="abs small" style="left:19px;top:61px;width:96px;font-size:3px;color:var(--teal)">Lorem No ceteros verterem his, sea eius iisque eu. Et vis stet dolorem perpetua, usu ea diam affert labores. No ceteros verterem his, sea eius iisque eu. Et vis stet dolorem perpetua, usu ea diam affert labores. No ceteros verterem his, sea eius iisque eu. Et vis stet dolorem perpetua, usu ea diam affert labores. No ceteros verterem his, sea eius iisque eu.</p>
  <div class="mlogo" style="left:184px;top:10px;font-size:3px">Marisa Dell</div>
</section>

<!-- 6 three bullet + image -->
<section class="slide c3 r2">
  <div class="title" style="left:17px;top:10px;font-size:8px;color:var(--teal)">THREE BULLET + IMAGE</div>
  <p class="abs tiny" style="left:26px;top:20px;font-size:2.3px">More information lorem ipsum has been the standard dummy text of</p>
  <div class="ring" style="left:16px;top:33px"></div>
  <div class="ring" style="left:16px;top:61px"></div>
  <div class="ring" style="left:16px;top:90px"></div>
  <div class="abs" style="left:38px;top:32px;width:78px"><p class="lead">Lorem ipsum dolor set</p><p class="tiny" style="color:var(--ink)">No ceteros verterem his, sea eius iisque eu. Et vis stet dolorem perpetua, usu ea</p></div>
  <div class="abs" style="left:38px;top:61px;width:78px"><p class="lead">Lorem ipsum dolor set</p><p class="tiny" style="color:var(--ink)">No ceteros verterem his, sea eius iisque eu. Et vis stet dolorem perpetua, usu ea</p></div>
  <div class="abs" style="left:38px;top:89px;width:78px"><p class="lead">Lorem ipsum dolor set</p><p class="tiny" style="color:var(--ink)">No ceteros verterem his, sea eius iisque eu. Et vis stet dolorem perpetua, usu ea</p></div>
  <div class="ph" style="left:124px;top:22px;width:94px;height:94px;border-radius:50%;border:2px solid var(--orange);background:radial-gradient(circle at 45% 50%,#f3f3f3,#9aa0a5 55%,#4b4f54)" role="img" aria-label="Photo of a hand using a tablet in a shop aisle"></div>
  <div class="foot"><span class="mini">Marisa Dell</span><span class="url">www.marisadellcoaching.com</span><span class="pg">6</span></div>
</section>

<!-- 7 theory -->
<section class="slide c1 r3">
  <div class="ph" style="left:0;top:0;width:236px;height:133px;background:linear-gradient(135deg,#f0a045,#c77a2e 45%,#6e4a2a 75%,#3a2a1e)" role="img" aria-label="Orange-tinted photo of a desk with coffee cup, laptop and notebook over a pier"></div>
  <div class="abs" style="left:-40px;top:-30px;width:150px;height:200px;border-radius:50%;background:rgba(247,148,29,.55)"></div>
  <div class="title" style="left:152px;top:6px;font-size:7px;color:#fff;line-height:1.1;text-align:center">THEORY ABOUT<br>OUR WORKSHOP</div>
  <div class="abs" style="left:18px;top:37px;width:78px;font-size:3.1px;line-height:1.35;color:#fff">
    <p style="margin-bottom:5px">• Lorem No ceteros verterem his, sea eius iisque eu. Et vis stet dolorem perpetua, usu ea diam affert labores.</p>
    <p style="margin-bottom:5px">• No ceteros verterem his, sea eius iisque eu. Et vis stet dolorem perpetua, usu ea diam affert labores.</p>
    <p style="margin-bottom:5px">• No ceteros verterem his, sea eius iisque eu. Et vis stet dolorem perpetua, usu ea diam affert labores.</p>
    <p>• Lorem No ceteros verterem his, sea eius iisque eu. Et vis stet dolorem perpetua, usu ea diam affert labores.</p>
  </div>
  <p class="abs" style="left:144px;top:37px;width:82px;font-size:3px;line-height:1.35;color:#fff;font-style:italic">Lorem ipsum dolor sit amet, consectetur adipiscing elit, sed do eiusmod tempor incididunt ut labore et dolore magna aliqua. Ut enim ad minim veniam. Lorem ipsum dolor sit amet, consectetur adipiscing elit, sed do eiusmod tempor incididunt ut labore et dolore magna aliqua. Ut enim ad minim veniam. Lorem ipsum dolor sit amet, consectetur adipiscing elit, sed do eiusmod tempor incididunt ut labore et dolore magna aliqua. Ut enim ad minim veniam. Lorem ipsum dolor sit amet, consectetur adipiscing elit, sed do eiusmod tempor incididunt ut labore et dolore magna aliqua.</p>
  <div class="foot"><span class="mini">Marisa Dell</span></div>
</section>

<!-- 8 section breaker -->
<section class="slide c2 r3">
  <div class="ph" style="left:0;top:0;width:236px;height:133px;background:linear-gradient(180deg,#2a2020,#a84a20 35%,#e2762a 55%,#1e1714 80%)" role="img" aria-label="Silhouette of a woman against a city skyline at sunset"></div>
  <div class="abs" style="left:-60px;top:-20px;width:165px;height:175px;border-radius:50%;background:#1b1b1b;border-right:4px solid var(--orange-deep)"></div>
  <div class="abs" style="left:15px;top:9px;width:47px;height:47px;border-radius:50%;background:var(--orange);color:#fff;font-size:22px;font-weight:600;text-align:center;line-height:47px">01</div>
  <div class="abs" style="left:12px;top:65px;font-size:9px;font-weight:600;color:#fff">Section breaker</div>
  <p class="abs" style="left:12px;top:78px;width:78px;font-size:4px;line-height:1.3;color:#fff">No ceteros verterem his, sea eius iisque eu. Et vis stet dolorem perpetua, usu at labores.</p>
</section>

<!-- 9 steps -->
<section class="slide c3 r3">
  <div class="ph" style="left:0;top:0;width:236px;height:82px;background:linear-gradient(160deg,#4a5560,#7c8a8c 45%,#5a6a4a)" role="img" aria-label="Photo of a misty mountain lake"></div>
  <div class="abs" style="left:0;top:68px;width:236px;height:65px;background:#fff"></div>
  <div class="title" style="left:98px;top:27px;font-size:14px;color:#fff;font-family:'Uncial Antiqua',serif;font-weight:400">STEPS</div>
  <p class="abs" style="left:60px;top:45px;width:116px;font-size:3.6px;line-height:1.3;color:#fff;font-style:italic;text-align:center">Lorem ipsum dolor sit amet, consectetur adipiscing elit, sed do eiusmod tempor incididunt ut labore et dolore magna aliqua. Ut enim ad minim veniam.</p>
  <div class="abs" style="left:22px;top:76px;width:10px;height:10px;border-radius:50%;background:#fff;border:1px solid var(--orange);font-size:4.5px;color:var(--orange);text-align:center;line-height:8px">1</div>
  <div class="abs" style="left:74px;top:76px;width:10px;height:10px;border-radius:50%;background:#fff;border:1px solid var(--orange);font-size:4.5px;color:var(--orange);text-align:center;line-height:8px">2</div>
  <div class="abs" style="left:126px;top:76px;width:10px;height:10px;border-radius:50%;background:#fff;border:1px solid var(--orange);font-size:4.5px;color:var(--orange);text-align:center;line-height:8px">3</div>
  <div class="abs" style="left:177px;top:76px;width:10px;height:10px;border-radius:50%;background:#fff;border:1px solid var(--orange);font-size:4.5px;color:var(--orange);text-align:center;line-height:8px">4</div>
  <div class="abs" style="left:22px;top:94px;width:38px"><p style="font-size:3.4px;font-weight:600;color:var(--orange)">Lorem ipsum dolor</p><p class="tiny" style="font-size:2.4px">No ceteros verterem his, sea eius iisque eu. Et vis stet dolorem perpetua, usu ea diam affert labor</p></div>
  <div class="abs" style="left:74px;top:94px;width:38px"><p style="font-size:3.4px;font-weight:600;color:var(--orange)">Lorem ipsum dolor</p><p class="tiny" style="font-size:2.4px">No ceteros verterem his, sea eius iisque eu. Et vis stet dolorem perpetua, usu ea diam affert labor</p></div>
  <div class="abs" style="left:126px;top:94px;width:38px"><p style="font-size:3.4px;font-weight:600;color:var(--orange)">Lorem ipsum dolor</p><p class="tiny" style="font-size:2.4px">No ceteros verterem his, sea eius iisque eu. Et vis stet dolorem perpetua, usu ea diam affert labor</p></div>
  <div class="abs" style="left:177px;top:94px;width:38px"><p style="font-size:3.4px;font-weight:600;color:var(--orange)">Lorem ipsum dolor</p><p class="tiny" style="font-size:2.4px">No ceteros verterem his, sea eius iisque eu. Et vis stet dolorem perpetua, usu ea diam affert labor</p></div>
  <div class="foot"><span class="mini">Marisa Dell</span><span class="url">www.marisadellcoaching.com</span><span class="pg">9</span></div>
</section>

<!-- 10 warm up -->
<section class="slide c1 r4">
  <div class="ph" style="left:0;top:0;width:236px;height:110px;background:linear-gradient(180deg,#3a4a2a,#6a8a3a 40%,#b84040 60%,#5a8a3a)" role="img" aria-label="Photo of a women's team jogging on a sports field"></div>
  <div class="abs" style="left:-40px;top:78px;width:316px;height:120px;border-radius:50%;background:#fff"></div>
  <div class="title" style="left:64px;top:10px;font-size:9px;color:#fff;font-style:italic">WARM UP ACTIVITY</div>
  <div class="abs" style="left:9px;top:58px;width:62px;height:62px;border-radius:50%;background:var(--teal);color:#fff;text-align:center;padding-top:22px">
    <p style="font-size:4.3px;font-weight:600">Lorem ipsum dolor set</p><p style="font-size:2.8px;line-height:1.3;padding:1px 6px">No ceteros verterem his, sea eius iisque eu. Et vis stet dolorem perpetua, usu ea diam affert labores.</p></div>
  <div class="abs" style="left:83px;top:58px;width:62px;height:62px;border-radius:50%;background:var(--slate);color:#fff;text-align:center;padding-top:22px">
    <p style="font-size:4.3px;font-weight:600">Lorem ipsum dolor set</p><p style="font-size:2.8px;line-height:1.3;padding:1px 6px">No ceteros verterem his, sea eius iisque eu. Et vis stet dolorem perpetua, usu ea diam affert labores.</p></div>
  <div class="abs" style="left:157px;top:58px;width:62px;height:62px;border-radius:50%;background:var(--orange);color:#fff;text-align:center;padding-top:22px">
    <p style="font-size:4.3px;font-weight:600">Lorem ipsum dolor set</p><p style="font-size:2.8px;line-height:1.3;padding:1px 6px">No ceteros verterem his, sea eius iisque eu. Et vis stet dolorem perpetua, usu ea diam affert labores.</p></div>
  <div class="abs" style="left:34px;top:63px;width:12px;height:12px;border-radius:50%;border:1px solid #fff"></div>
  <div class="abs" style="left:108px;top:63px;width:12px;height:12px;border-radius:50%;border:1px solid #fff"></div>
  <div class="abs" style="left:182px;top:63px;width:12px;height:12px;border-radius:50%;border:1px solid #fff"></div>
  <div class="foot"><span class="mini">Marisa Dell</span><span class="url">www.marisadellcoaching.com</span><span class="pg">10</span></div>
</section>

<!-- 11 activity 2 -->
<section class="slide c2 r4">
  <div class="title" style="left:88px;top:7px;font-size:8px">ACTIVITY #2</div>
  <p class="abs tiny" style="left:66px;top:18px;font-size:2.2px">LOREM IPSUM, GIVING INFORMATION ON ITS ORIGINS, AS WELL AS RANDOM TEXT</p>
  <div class="ph" style="left:0;top:31px;width:39px;height:39px;background:linear-gradient(135deg,#7a5a40,#d6c2a8)" role="img" aria-label="Photo of a desk with coffee and notes"></div>
  <div class="cell" style="left:39px;top:31px;width:39px;height:39px;background:var(--orange)"><b>Content Text</b><p>Lorem Ipsum is simply dummy text of the printing and typesetting industry</p></div>
  <div class="ph" style="left:78px;top:31px;width:39px;height:39px;background:linear-gradient(180deg,#c9d3d8,#4f6b6a)" role="img" aria-label="Photo of a mountain lake pier"></div>
  <div class="cell" style="left:117px;top:31px;width:39px;height:39px;background:var(--slate)"><b>Content Text</b><p>Lorem Ipsum is simply dummy text of the printing and typesetting industry</p></div>
  <div class="ph" style="left:156px;top:31px;width:40px;height:39px;background:linear-gradient(160deg,#5a6670,#8a9a90)" role="img" aria-label="Photo of a misty mountain valley"></div>
  <div class="cell" style="left:196px;top:31px;width:40px;height:39px;background:var(--lavender)"><b>Content Text</b><p>Lorem Ipsum is simply dummy text of the printing and typesetting industry</p></div>
  <div class="cell" style="left:0;top:70px;width:39px;height:39px;background:var(--plum)"><b>Content Text</b><p>Lorem Ipsum is simply dummy text of the printing and typesetting industry</p></div>
  <div class="ph" style="left:39px;top:70px;width:39px;height:39px;background:linear-gradient(140deg,#3f5a2a,#8aa064)" role="img" aria-label="Photo of a woman among green foliage"></div>
  <div class="cell" style="left:78px;top:70px;width:39px;height:39px;background:var(--teal)"><b>Content Text</b><p>Lorem Ipsum is simply dummy text of the printing and typesetting industry</p></div>
  <div class="ph" style="left:117px;top:70px;width:39px;height:39px;background:linear-gradient(160deg,#e8e8e6,#6b6b67)" role="img" aria-label="Photo of a bright office"></div>
  <div class="cell" style="left:156px;top:70px;width:40px;height:39px;background:var(--yellow)"><b>Content Text</b><p>Lorem Ipsum is simply dummy text of the printing and typesetting industry</p></div>
  <div class="ph" style="left:196px;top:70px;width:40px;height:39px;background:linear-gradient(180deg,#a84a20,#e2762a 50%,#1e1714)" role="img" aria-label="Photo of a silhouette at sunset"></div>
  <div class="foot"><span class="mini">Marisa Dell</span><span class="url">www.marisadellcoaching.com</span><span class="pg">22</span></div>
</section>

<!-- 12 activity 3 -->
<section class="slide c3 r4">
  <div class="title" style="left:88px;top:7px;font-size:8px">ACTIVITY #3</div>
  <p class="abs tiny" style="left:66px;top:18px;font-size:2.2px">LOREM IPSUM, GIVING INFORMATION ON ITS ORIGINS, AS WELL AS RANDOM TEXT</p>
  <div class="ph" style="left:0;top:31px;width:117px;height:78px;background:linear-gradient(180deg,#d9e2e6,#6d8a8a 45%,#3d5a55 70%,#5a4a3a)" role="img" aria-label="Photo of a person on a pier at a mountain lake"></div>
  <div class="cell" style="left:117px;top:31px;width:39px;height:39px;background:var(--teal)"><b>Content Text</b><p>Lorem Ipsum is simply dummy text of the printing and typesetting industry</p></div>
  <div class="ph" style="left:156px;top:31px;width:40px;height:39px;background:linear-gradient(135deg,#7a5a40,#d6c2a8)" role="img" aria-label="Photo of a desk with coffee and notes"></div>
  <div class="cell" style="left:196px;top:31px;width:40px;height:39px;background:var(--plum)"><b>Content Text</b><p>Lorem Ipsum is simply dummy text of the printing and typesetting industry</p></div>
  <div class="ph" style="left:117px;top:70px;width:39px;height:39px;background:linear-gradient(140deg,#3f5a2a,#8aa064)" role="img" aria-label="Photo of a woman among green foliage"></div>
  <div class="cell" style="left:156px;top:70px;width:40px;height:39px;background:var(--orange)"><b>Content Text</b><p>Lorem Ipsum is simply dummy text of the printing and typesetting industry</p></div>
  <div class="ph" style="left:196px;top:70px;width:40px;height:39px;background:linear-gradient(160deg,#e8e8e6,#6b6b67)" role="img" aria-label="Photo of a bright office"></div>
  <div class="foot"><span class="mini">Marisa Dell</span><span class="url">www.marisadellcoaching.com</span><span class="pg">23</span></div>
</section>

<!-- 13 four blocks -->
<section class="slide c1 r5">
  <div class="title" style="left:21px;top:9px;font-size:8px">FOUR BLOCKS TO EXPRESS YOUR IDEAS</div>
  <p class="abs tiny" style="left:87px;top:20px;font-size:2.3px">Also you can add a subtitle, don't need? Just Delete</p>
  <div class="cell" style="left:0;top:37px;width:59px;height:21px;background:var(--orange);padding-left:20px"><b style="padding-top:3px">Lorem ipsum<br>dolor set</b></div>
  <div class="cell" style="left:59px;top:37px;width:59px;height:21px;background:var(--teal);padding-left:18px"><b style="padding-top:3px">Lorem ipsum<br>dolor set</b></div>
  <div class="cell" style="left:118px;top:37px;width:59px;height:21px;background:var(--plum);padding-left:18px"><b style="padding-top:3px">Lorem ipsum<br>dolor set</b></div>
  <div class="cell" style="left:177px;top:37px;width:59px;height:21px;background:var(--yellow);padding-left:18px"><b style="padding-top:3px">Lorem ipsum<br>dolor set</b></div>
  <p class="abs tiny" style="left:8px;top:64px;width:47px;font-size:2.8px;text-align:justify">No ceteros verterem his, sea eius iisque eu. Et vis stet dolorem perpetua, usu ea diam affert labores. Has quidam vulputate no, sea salutatus philosophia eu, quas consul ei duo. Quas inductum vis no, oblique adipiscing et vel, urbanitas mediocritatem nam an. Nec aperiri definiebas percipitur at.</p>
  <p class="abs tiny" style="left:67px;top:64px;width:47px;font-size:2.8px;text-align:justify">No ceteros verterem his, sea eius iisque eu. Et vis stet dolorem perpetua, usu ea diam affert labores. Has quidam vulputate no, sea salutatus philosophia eu, quas consul ei duo. Quas inductum vis no, oblique adipiscing et vel, urbanitas mediocritatem nam an. Nec aperiri definiebas percipitur at.</p>
  <p class="abs tiny" style="left:126px;top:64px;width:47px;font-size:2.8px;text-align:justify">No ceteros verterem his, sea eius iisque eu. Et vis stet dolorem perpetua, usu ea diam affert labores. Has quidam vulputate no, sea salutatus philosophia eu, quas consul ei duo. Quas inductum vis no, oblique adipiscing et vel, urbanitas mediocritatem nam an. Nec aperiri definiebas percipitur at.</p>
  <p class="abs tiny" style="left:185px;top:64px;width:47px;font-size:2.8px;text-align:justify">No ceteros verterem his, sea eius iisque eu. Et vis stet dolorem perpetua, usu ea diam affert labores. Has quidam vulputate no, sea salutatus philosophia eu, quas consul ei duo. Quas inductum vis no, oblique adipiscing et vel, urbanitas mediocritatem nam an. Nec aperiri definiebas percipitur at.</p>
  <div class="foot"><span class="mini">Marisa Dell</span><span class="url">www.marisadellcoaching.com</span><span class="pg">14</span></div>
</section>

<!-- 14 four blocks coloured -->
<section class="slide c2 r5">
  <div class="title" style="left:21px;top:9px;font-size:8px">FOUR BLOCKS TO EXPRESS YOUR IDEAS</div>
  <p class="abs tiny" style="left:87px;top:20px;font-size:2.3px">Also you can add a subtitle, don't need? Just Delete</p>
  <div class="cell" style="left:0;top:34px;width:59px;height:99px;background:var(--orange);padding:20px 6px 0"><b style="font-size:3.8px">Lorem ipsum dolor set</b><p style="text-align:justify">No ceteros verterem his, sea eius iisque eu. Et vis stet dolorem perpetua, usu ea diam affert labores. Has quidam vulputate no, sea salutatus philosophia eu, quas consul ei duo. Quas inductum vis no, oblique adipiscing et vel, urbanitas mediocritatem nam an. Nec aperiri definiebas percipitur at. Sea prima mutat sadipscing ne.</p></div>
  <div class="cell" style="left:59px;top:34px;width:59px;height:99px;background:var(--plum);padding:20px 6px 0"><b style="font-size:3.8px">Lorem ipsum dolor set</b><p style="text-align:justify">No ceteros verterem his, sea eius iisque eu. Et vis stet dolorem perpetua, usu ea diam affert labores. Has quidam vulputate no, sea salutatus philosophia eu, quas consul ei duo. Quas inductum vis no, oblique adipiscing et vel, urbanitas mediocritatem nam an. Nec aperiri definiebas percipitur at. Sea prima mutat sadipscing ne.</p></div>
  <div class="cell" style="left:118px;top:34px;width:59px;height:99px;background:var(--teal);padding:20px 6px 0"><b style="font-size:3.8px">Lorem ipsum dolor set</b><p style="text-align:justify">No ceteros verterem his, sea eius iisque eu. Et vis stet dolorem perpetua, usu ea diam affert labores. Has quidam vulputate no, sea salutatus philosophia eu, quas consul ei duo. Quas inductum vis no, oblique adipiscing et vel, urbanitas mediocritatem nam an. Nec aperiri definiebas percipitur at. Sea prima mutat sadipscing ne.</p></div>
  <div class="cell" style="left:177px;top:34px;width:59px;height:99px;background:var(--yellow);padding:20px 6px 0"><b style="font-size:3.8px">Lorem ipsum dolor set</b><p style="text-align:justify">No ceteros verterem his, sea eius iisque eu. Et vis stet dolorem perpetua, usu ea diam affert labores. Has quidam vulputate no, sea salutatus philosophia eu, quas consul ei duo. Quas inductum vis no, oblique adipiscing et vel, urbanitas mediocritatem nam an. Nec aperiri definiebas percipitur at. Sea prima mutat sadipscing ne.</p></div>
  <div class="abs" style="left:23px;top:38px;width:12px;height:10px;border:1px solid #fff"></div>
  <div class="abs" style="left:83px;top:38px;width:12px;height:10px;border:1px solid #fff"></div>
  <div class="abs" style="left:141px;top:37px;width:12px;height:12px;border-radius:50%;border:1px solid #fff"></div>
  <div class="abs" style="left:200px;top:37px;width:12px;height:12px;border-radius:50%;border:1px solid #fff"></div>
  <div class="mlogo" style="left:20px;top:126px;font-size:2.8px;color:#fff">Marisa Dell</div>
</section>

<!-- 15 four spaces -->
<section class="slide c3 r5">
  <div class="title" style="left:59px;top:8px;font-size:8px">FOUR <span style="color:var(--orange)">SPACES</span> FOR TEXT</div>
  <p class="abs tiny" style="left:44px;top:19px;font-size:2.2px">More information lorem ipsum has been the standard dummy text of the printing industry.</p>
  <div class="cell" style="left:13px;top:30px;width:102px;height:38px;background:var(--plum);padding:10px 4px 0 22px"><b style="font-size:4px">Lorem ipsum dolor set</b><p style="font-size:3px">No ceteros verterem his, sea eius iisque eu. Et vis stet dolorem perpetua, usu ea diam affert labores.</p></div>
  <div class="cell" style="left:118px;top:30px;width:102px;height:38px;background:var(--orange);padding:10px 4px 0 22px"><b style="font-size:4px">Lorem ipsum dolor set</b><p style="font-size:3px">No ceteros verterem his, sea eius iisque eu. Et vis stet dolorem perpetua, usu ea diam affert labores.</p></div>
  <div class="cell" style="left:13px;top:72px;width:102px;height:38px;background:var(--teal);padding:10px 4px 0 22px"><b style="font-size:4px">Lorem ipsum dolor set</b><p style="font-size:3px">No ceteros verterem his, sea eius iisque eu. Et vis stet dolorem perpetua, usu ea diam affert labores.</p></div>
  <div class="cell" style="left:118px;top:72px;width:102px;height:38px;background:var(--slate);padding:10px 4px 0 22px"><b style="font-size:4px">Lorem ipsum dolor set</b><p style="font-size:3px">No ceteros verterem his, sea eius iisque eu. Et vis stet dolorem perpetua, usu ea diam affert labores.</p></div>
  <div class="abs" style="left:18px;top:43px;width:12px;height:12px;border-radius:50%;border:1.4px solid #fff"></div>
  <div class="abs" style="left:123px;top:43px;width:12px;height:12px;border-radius:50%;border:1.4px solid #fff"></div>
  <div class="abs" style="left:18px;top:85px;width:12px;height:12px;border-radius:50%;border:1.4px solid #fff"></div>
  <div class="abs" style="left:123px;top:85px;width:12px;height:12px;border-radius:50%;border:1.4px solid #fff"></div>
  <div class="foot"><span class="mini">Marisa Dell</span><span class="url">www.marisadellcoaching.com</span><span class="pg">12</span></div>
</section>

<!-- 16 activity 4 -->
<section class="slide c1 r6">
  <div class="title" style="left:88px;top:9px;font-size:8px">ACTIVITY #4</div>
  <p class="abs tiny" style="left:66px;top:20px;font-size:2.2px">LOREM IPSUM, GIVING INFORMATION ON ITS ORIGINS, AS WELL AS RANDOM TEXT</p>
  <div class="cell" style="left:0;top:30px;width:59px;height:40px;background:var(--orange)"><b>Lorem ipsum dolor set</b><p>No ceteros verterem his, sea eius iisque eu. Et vis stet dolorem perpetua, usu ea diam affert labores.</p></div>
  <div class="cell" style="left:59px;top:30px;width:59px;height:40px;background:var(--plum)"><b>Lorem ipsum dolor set</b><p>No ceteros verterem his, sea eius iisque eu. Et vis stet dolorem perpetua, usu ea diam affert labores.</p></div>
  <div class="cell" style="left:118px;top:30px;width:59px;height:40px;background:var(--slate)"><b>Lorem ipsum dolor set</b><p>No ceteros verterem his, sea eius iisque eu. Et vis stet dolorem perpetua, usu ea diam affert labores.</p></div>
  <div class="cell" style="left:177px;top:30px;width:59px;height:40px;background:var(--yellow)"><b>Lorem ipsum dolor set</b><p>No ceteros verterem his, sea eius iisque eu. Et vis stet dolorem perpetua, usu ea diam affert labores.</p></div>
  <div class="cell" style="left:0;top:70px;width:59px;height:41px;background:var(--yellow)"><b>Lorem ipsum dolor set</b><p>No ceteros verterem his, sea eius iisque eu. Et vis stet dolorem perpetua, usu ea diam affert labores.</p></div>
  <div class="cell" style="left:59px;top:70px;width:59px;height:41px;background:var(--slate)"><b>Lorem ipsum dolor set</b><p>No ceteros verterem his, sea eius iisque eu. Et vis stet dolorem perpetua, usu ea diam affert labores.</p></div>
  <div class="cell" style="left:118px;top:70px;width:59px;height:41px;background:var(--plum)"><b>Lorem ipsum dolor set</b><p>No ceteros verterem his, sea eius iisque eu. Et vis stet dolorem perpetua, usu ea diam affert labores.</p></div>
  <div class="cell" style="left:177px;top:70px;width:59px;height:41px;background:var(--orange)"><b>Lorem ipsum dolor set</b><p>No ceteros verterem his, sea eius iisque eu. Et vis stet dolorem perpetua, usu ea diam affert labores.</p></div>
  <div class="foot"><span class="mini">Marisa Dell</span><span class="url">www.marisadellcoaching.com</span><span class="pg">24</span></div>
</section>

<!-- 17 teal two columns -->
<section class="slide c2 r6" style="background:var(--teal)">
  <div class="display" style="left:19px;top:24px;font-size:10px">IT'S IMPORTANT<br>EXPRESS YOUR IDEAS WITH FEW<br>WORDS</div>
  <p class="abs" style="left:18px;top:68px;width:92px;font-size:3px;line-height:1.35;color:#fff;text-align:justify">Lorem Ipsum is simply dummy text of the printing and typesetting industry. No ceteros verterem his, sea eius iisque eu. Et vis stet dolorem perpetua, usu ea diam affert labores. Lorem Ipsum is simply dummy text of the printing and typesetting industry. No ceteros verterem his, sea eius iisque eu. Et vis stet dolorem perpetua, usu ea diam affert labores. No ceteros verterem his, sea eius iisque eu.</p>
  <p class="abs" style="left:127px;top:68px;width:92px;font-size:3px;line-height:1.35;color:#fff;text-align:justify">Lorem Ipsum is simply dummy text of the printing and typesetting industry. No ceteros verterem his, sea eius iisque eu. Et vis stet dolorem perpetua, usu ea diam affert labores. Lorem Ipsum is simply dummy text of the printing and typesetting industry. No ceteros verterem his, sea eius iisque eu. Et vis stet dolorem perpetua, usu ea diam affert labores. No ceteros verterem his, sea eius iisque eu.</p>
  <div class="foot dark"><span class="mini">Marisa Dell</span><span class="url">www.marisadellcoaching.com</span><span class="pg">16</span></div>
</section>

<!-- 18 teal left title -->
<section class="slide c3 r6" style="background:var(--teal)">
  <div class="display" style="left:18px;top:38px;font-size:11px">IT'S<br>IMPORTANT<br>EXPRESS YOUR<br>IDEA WITH<br>FEW WORDS</div>
  <p class="abs" style="left:128px;top:29px;width:92px;font-size:3px;line-height:1.4;color:#fff;text-align:justify">Lorem Ipsum is simply dummy text of the printing and typesetting industry. No ceteros verterem his, sea eius iisque eu. Et vis stet dolorem perpetua, usu ea diam affert labores. Lorem Ipsum is simply dummy text of the printing and typesetting industry. No ceteros verterem his, sea eius iisque eu. Et vis stet dolorem perpetua, usu ea diam affert labores. No ceteros verterem his, sea eius iisque eu. Et vis stet dolorem perpetua, usu ea diam affert labores. No ceteros verterem his, sea eius iisque eu. Et vis stet dolorem perpetua, usu ea diam affert labores. Et vis stet dolorem perpetua, usu ea diam eius iisque eu.</p>
  <div class="foot dark"><span class="mini">Marisa Dell</span><span class="url">www.marisadellcoaching.com</span><span class="pg">15</span></div>
</section>

<!-- 19 plum four bullets and text -->
<section class="slide c1 r7" style="background:var(--plum-bright)">
  <div class="display" style="left:18px;top:29px;font-size:10px">EXPRESS<br>YOUR IDEA IN<br>FOUR BULLETS<br>AND TEXT</div>
  <p class="abs" style="left:18px;top:74px;width:82px;font-size:3px;line-height:1.35;color:#fff">Lorem Ipsum is simply dummy text of the printing and typesetting industry. No ceteros verterem his, sea eius iisque eu. Et vis stet dolorem perpetua, usu ea diam affert labores. Lorem Ipsum is simply dummy text of the printing and typesetting industry. Lorem Ipsum is simply dummy</p>
  <div class="dot" style="left:116px;top:32px"></div>
  <div class="dot" style="left:116px;top:51px"></div>
  <div class="dot" style="left:116px;top:70px"></div>
  <div class="dot" style="left:116px;top:89px"></div>
  <p class="abs" style="left:125px;top:31px;width:96px;font-size:3px;line-height:1.35;color:#fff">Lorem Ipsum is simply dummy text of the printing and typesetting industry. No ceteros verterem his, sea eius iisque eu. simply dummy text of the printing</p>
  <p class="abs" style="left:125px;top:50px;width:96px;font-size:3px;line-height:1.35;color:#fff">Lorem Ipsum is simply dummy text of the printing and typesetting industry. No ceteros verterem his, sea eius iisque eu. simply dummy text of the printing</p>
  <p class="abs" style="left:125px;top:69px;width:96px;font-size:3px;line-height:1.35;color:#fff">Lorem Ipsum is simply dummy text of the printing and typesetting industry. No ceteros verterem his, sea eius iisque eu. simply dummy text of the printing</p>
  <p class="abs" style="left:125px;top:88px;width:96px;font-size:3px;line-height:1.35;color:#fff">Lorem Ipsum is simply dummy text of the printing and typesetting industry. No ceteros verterem his, sea eius iisque eu. simply dummy text of the printing</p>
  <div class="foot dark"><span class="mini">Marisa Dell</span><span class="url">www.marisadellcoaching.com</span><span class="pg">17</span></div>
</section>

<!-- 20 plum four bullets -->
<section class="slide c2 r7" style="background:var(--plum-bright)">
  <div class="title" style="left:19px;top:10px;font-size:8px;color:var(--orange)">FOUR BULLETS TO EXPRESS YOUR IDEAS</div>
  <p class="abs" style="left:86px;top:21px;font-size:2.3px;color:var(--orange)">Also you can add a subtitle, don't need? Just Delete</p>
  <div class="dot" style="left:36px;top:34px"></div>
  <div class="dot" style="left:36px;top:53px"></div>
  <div class="dot" style="left:36px;top:72px"></div>
  <div class="dot" style="left:36px;top:91px"></div>
  <p class="abs" style="left:45px;top:33px;width:150px;font-size:3px;line-height:1.35;color:#fff">Lorem Ipsum is simply dummy text of the printing and typesetting industry. No ceteros verterem his, sea eius iisque eu. Et vis stet dolorem perpetua, usu ea diam affert labores. No ceteros verterem his, sea eius iisque</p>
  <p class="abs" style="left:45px;top:52px;width:150px;font-size:3px;line-height:1.35;color:#fff">Lorem Ipsum is simply dummy text of the printing and typesetting industry. No ceteros verterem his, sea eius iisque eu. Et vis stet dolorem perpetua, usu ea diam affert labores. No ceteros verterem his, sea eius iisque</p>
  <p class="abs" style="left:45px;top:71px;width:150px;font-size:3px;line-height:1.35;color:#fff">Lorem Ipsum is simply dummy text of the printing and typesetting industry. No ceteros verterem his, sea eius iisque eu. Et vis stet dolorem perpetua, usu ea diam affert labores. No ceteros verterem his, sea eius iisque</p>
  <p class="abs" style="left:45px;top:90px;width:150px;font-size:3px;line-height:1.35;color:#fff">Lorem Ipsum is simply dummy text of the printing and typesetting industry. No ceteros verterem his, sea eius iisque eu. Et vis stet dolorem perpetua, usu ea diam affert labores. No ceteros verterem his, sea eius iisque</p>
  <div class="foot dark"><span class="mini">Marisa Dell</span><span class="url">www.marisadellcoaching.com</span><span class="pg">18</span></div>
</section>

<!-- 21 plum two text columns -->
<section class="slide c3 r7" style="background:var(--plum-bright)">
  <div class="title" style="left:19px;top:10px;font-size:8px;color:var(--orange)">EXPRESS YOUR IDEAS IN TWO TEXT COLUMNS</div>
  <p class="abs" style="left:86px;top:21px;font-size:2.3px;color:var(--orange)">Also you can add a subtitle, don't need? Just Delete</p>
  <p class="abs" style="left:18px;top:34px;font-size:4px;color:var(--orange)">No ceteros verterem</p>
  <p class="abs" style="left:127px;top:34px;font-size:4px;color:var(--orange)">No ceteros verterem</p>
  <p class="abs" style="left:18px;top:40px;width:92px;font-size:3px;line-height:1.35;color:#fff;text-align:justify">Lorem Ipsum is simply dummy text of the printing and typesetting industry. No ceteros verterem his, sea eius iisque eu. Et vis stet dolorem perpetua, usu ea diam affert labores. Lorem Ipsum is simply dummy text of the printing and typesetting industry. No ceteros verterem his, sea eius iisque eu. Et vis stet dolorem perpetua, usu ea diam affert labores. No ceteros verterem his, sea eius iisque eu. Et vis stet dolorem perpetua, usu ea diam affert labores. No ceteros verterem his, sea eius iisque eu.</p>
  <p class="abs" style="left:127px;top:40px;width:92px;font-size:3px;line-height:1.35;color:#fff;text-align:justify">Lorem Ipsum is simply dummy text of the printing and typesetting industry. No ceteros verterem his, sea eius iisque eu. Et vis stet dolorem perpetua, usu ea diam affert labores. Lorem Ipsum is simply dummy text of the printing and typesetting industry. No ceteros verterem his, sea eius iisque eu. Et vis stet dolorem perpetua, usu ea diam affert labores. No ceteros verterem his, sea eius iisque eu. Et vis stet dolorem perpetua, usu ea diam affert labores.</p>
  <div class="foot dark"><span class="mini">Marisa Dell</span><span class="url">www.marisadellcoaching.com</span><span class="pg">19</span></div>
</section>

</body>
</html>
```